Neuroscience laboratory website

The "Speech, Thought and Nerve Lab" (aka, SoTeN Lab) is looking for a web site design. We are a cognitive neuroscience of language laboratory, which means we study the brain circuits involved in language comprehension. We need a professional-looking web presence where we can introduce the kind of research we do, list our publications, present our research team, present the current experiments that are being conducted and present our lab blog. Our current web site is displayed at http://soten-lab.example-host.io/soten.lab.example-host.io/. The new design should be a net improvement over the existing one.
Updates

Project Deadline Extended
Reason: Error was made when posting the contest. I am rectifying it now.

Target Market(s)

Primary audience will be other academics and university-age students interested in learning more about the lab, but it should also target the general adult public based in western countries.

Industry/Entity Type

Laboratory

Colors

Designer to choose colors to be used in the design.

Requirements
Nice to have
• It would be nice if the design could be informed by at least one of all the following concepts: Human languages/scripts, mind, brain, neuroimaging and brain signals (like electroencephalogram), neuroscience, science, knowledge.

Word or visual play with the acronym of the lab (SoTeN) would be permissable, if a good idea can be extracted out of it.
Should not have
• Design should have a clean background. It should use large framing images very sparingly, if at all.

```html
<!DOCTYPE html>
<html lang="en">
<head>
<meta charset="utf-8">
<title>People — Speech, Thought and Nerve Lab</title>
<link rel="stylesheet" href="https://fonts.googleapis.com/css2?family=Fira+Sans+Condensed:ital,wght@0,400;0,500;0,600;0,700;1,400&family=Open+Sans:ital@1&display=swap">
<style>
:root{
  --brand:#2d5a80;
  --brand-dark:#1f3f5c;
  --nav-top:#4a7fab;
  --nav-bottom:#2e5b82;
  --ink:#111;
  --text:#333;
  --muted:#666;
  --band:#ebebeb;
  --white:#fff;
}
*{margin:0;padding:0;box-sizing:border-box}
html,body{width:985px;height:1200px;overflow:hidden;background:var(--white)}
body{position:relative;font-family:"Fira Sans Condensed",sans-serif;color:var(--text)}
.abs{position:absolute}

.logo{left:130px;top:10px;width:170px;height:58px;background:#fafafa;text-align:center}
.logo-mark{display:block;width:12px;height:12px;border-radius:50%;background:var(--brand);margin:12px auto 6px}
.logo-name{font-size:12.5px;color:var(--brand)}

.main-nav{left:330px;top:27px;width:536px;height:33px;border-radius:4px;
  background:linear-gradient(var(--nav-top),var(--nav-bottom));display:flex;overflow:hidden;
  box-shadow:0 1px 2px rgba(0,0,0,.3)}
.main-nav a{color:var(--white);text-decoration:none;font-size:13px;display:flex;align-items:center;justify-content:center;
  border-right:1px solid rgba(0,0,0,.2)}
.main-nav a:last-child{border-right:0}
.main-nav a.is-active{background:var(--brand-dark);font-weight:600}

.page-title{left:138px;top:88px;font-size:67px;font-weight:700;color:var(--brand);letter-spacing:-1px}
.section-title{left:144px;font-size:30px;font-weight:600;color:var(--ink);letter-spacing:-.5px}

.member{width:180px}
.member-name{font-size:17.5px;font-weight:600;color:var(--brand);line-height:20px}
.member-name.is-muted{color:#444}
.member-role{font-size:12.5px;font-style:italic;color:var(--muted);line-height:16px}
.member-bio{margin-top:6px;font-size:9.5px;line-height:11px;color:var(--text);width:150px}

.testimonial-band{left:0;top:948px;width:985px;height:227px;background:var(--band)}
.band-shade{left:170px;top:940px;width:420px;height:10px;background:radial-gradient(ellipse at center,rgba(0,0,0,.12),transparent 70%)}
.quote-badge{left:349px;top:928px;width:30px;height:30px;border-radius:50%;background:var(--white);
  box-shadow:0 1px 3px rgba(0,0,0,.2);text-align:center;font-family:Georgia,serif;font-size:24px;font-weight:700;
  color:var(--brand);line-height:38px}
.portrait-frame{left:155px;top:995px;width:74px;height:78px;background:var(--white);border-radius:4px;padding:4px;
  box-shadow:0 2px 4px rgba(0,0,0,.25)}
.portrait{width:100%;height:100%;background:linear-gradient(160deg,#cfdbe6,#9fb6ca)}
.quote-text{left:263px;top:1003px;width:280px;font-family:"Open Sans",sans-serif;font-style:italic;font-size:10.5px;line-height:13.5px;color:#555}
.quote-author{left:160px;top:1096px;width:70px;text-align:center}
.quote-author .sig{font-family:Georgia,serif;font-style:italic;font-size:13px;color:#555}
.quote-author .org{font-size:7px;font-weight:600;color:var(--brand)}
.slider-dots{left:263px;top:1100px;display:flex;gap:3px}
.slider-dots span{width:8px;height:8px;border-radius:50%;background:#ccc}
.slider-dots span:first-child{background:#b5b5b5}
.social{left:385px;top:1094px;display:flex;align-items:center;gap:2px;font-size:9.5px;color:#444}
.social .label{margin-right:13px}
.social .icon{width:20px;height:20px;border-radius:4px;background:var(--brand)}
.social .icon.alt{background:#b33a2e}
.divider{left:581px;top:972px;height:171px;border-left:1px dotted #888}

.newsletter{left:620px;top:980px;width:220px;text-align:center}
.newsletter h3{font-size:14px;font-weight:600;color:var(--brand);text-transform:uppercase}
.newsletter p{font-size:12.5px;color:var(--muted)}
.newsletter-input{left:634px;top:1034px;width:195px;height:27px;background:var(--white);border:1px solid #ddd}
.newsletter-note{left:642px;top:1073px;width:190px;font-size:9px;font-style:italic;line-height:10.5px;color:#888}
.newsletter-button{left:675px;top:1119px;width:114px;height:27px;background:var(--brand);color:var(--white);
  font-size:13px;font-weight:600;display:flex;align-items:center;justify-content:center}

.site-footer{left:0;top:1175px;width:985px;height:25px;background:var(--brand);color:var(--white);font-size:7.5px}
.site-footer span{position:absolute;top:9px}
</style>
</head>
<body>

<header>
  <div class="abs logo"><span class="logo-mark"></span><span class="logo-name">Speech, Thought &amp; Nerve Lab</span></div>
  <nav class="abs main-nav">
    <a href="#" style="width:76px">Home</a>
    <a href="#" class="is-active" style="width:83px">People</a>
    <a href="#" style="width:104px">Publications</a>
    <a href="#" style="width:97px">Research</a>
    <a href="#" style="width:92px">Blog</a>
    <a href="#" style="width:84px">Repository</a>
  </nav>
</header>

<main>
  <h1 class="abs page-title">People</h1>

  <h2 class="abs section-title" style="top:188px">Researchers</h2>
  <article class="abs member" style="left:145px;top:236px"><h3 class="member-name">Dario Almont</h3><p class="member-role">Principal Investigator</p><p class="member-bio">Temporibus autem quibusdam et aut officiis debitis aut rerum necessitatibus saepe eveniet ut et voluptates repudiandae sint et molestiae non recusandae.</p></article>
  <article class="abs member" style="left:345px;top:236px"><h3 class="member-name">Kevan Schroder</h3><p class="member-role">Postdoc</p><p class="member-bio">Temporibus autem quibusdam et aut officiis debitis aut rerum necessitatibus saepe eveniet ut et voluptates repudiandae sint et molestiae non recusandae.</p></article>
  <article class="abs member" style="left:561px;top:236px"><h3 class="member-name">Mark Tolliver</h3><p class="member-role">Postdoc</p><p class="member-bio">Temporibus autem quibusdam et aut officiis debitis aut rerum necessitatibus saepe eveniet ut et voluptates repudiandae sint et molestiae non recusandae.</p></article>

  <h2 class="abs section-title" style="top:369px">Local Affiliates and Collaborators</h2>
  <article class="abs member" style="left:145px;top:419px"><h3 class="member-name">Amin Idrani</h3><p class="member-role">Associate Professor, GUSU</p><p class="member-bio">Temporibus autem quibusdam et aut officiis debitis aut rerum necessitatibus saepe eveniet ut et voluptates repudiandae sint et molestiae non recusandae.</p></article>
  <article class="abs member" style="left:345px;top:419px"><h3 class="member-name">Simon Pollard-Ames</h3><p class="member-role">Postdoc, NeLab</p><p class="member-bio">Temporibus autem quibusdam et aut officiis debitis aut rerum necessitatibus saepe eveniet ut et voluptates repudiandae sint et molestiae non recusandae.</p></article>
  <article class="abs member" style="left:561px;top:419px"><h3 class="member-name">Jonah Kingsley</h3><p class="member-role">Research Assistant, NeLab</p><p class="member-bio">Temporibus autem quibusdam et aut officiis debitis aut rerum necessitatibus saepe eveniet ut et voluptates repudiandae sint et molestiae non recusandae.</p></article>

  <h2 class="abs section-title" style="top:554px">Visitors</h2>
  <article class="abs member" style="left:145px;top:602px"><h3 class="member-name is-muted">Amin Idrani</h3><p class="member-role">Associate Professor, GUSU</p><p class="member-bio">Temporibus autem quibusdam et aut officiis debitis aut rerum necessitatibus saepe eveniet ut et voluptates repudiandae sint et molestiae non recusandae.</p></article>
  <article class="abs member" style="left:345px;top:602px"><h3 class="member-name">Simon Pollard-Ames</h3><p class="member-role">Postdoc, NeLab</p><p class="member-bio">Temporibus autem quibusdam et aut officiis debitis aut rerum necessitatibus saepe eveniet ut et voluptates repudiandae sint et molestiae non recusandae.</p></article>
  <article class="abs member" style="left:561px;top:602px"><h3 class="member-name is-muted">Jonah Kingsley</h3><p class="member-role">Research Assistant, NeLab</p><p class="member-bio">Temporibus autem quibusdam et aut officiis debitis aut rerum necessitatibus saepe eveniet ut et voluptates repudiandae sint et molestiae non recusandae.</p></article>

  <h2 class="abs section-title" style="top:739px">Undergraduates</h2>
  <article class="abs member" style="left:145px;top:792px"><h3 class="member-name">Jenna Obrecht</h3><p class="member-role">Capstone project</p><p class="member-bio">Temporibus autem quibusdam et aut officiis debitis aut rerum necessitatibus saepe eveniet ut et voluptates repudiandae sint et molestiae non recusandae.</p></article>
  <article class="abs member" style="left:331px;top:792px"><h3 class="member-name">Hana Kyeong Pyo</h3><p class="member-role">Capstone project</p><p class="member-bio">Temporibus autem quibusdam et aut officiis debitis aut rerum necessitatibus saepe eveniet ut et voluptates repudiandae sint et molestiae non recusandae.</p></article>
  <article class="abs member" style="left:518px;top:792px"><h3 class="member-name">Valeria Edgars</h3><p class="member-role">Undergraduate researcher</p><p class="member-bio">Temporibus autem quibusdam et aut officiis debitis aut rerum necessitatibus saepe eveniet ut et voluptates repudiandae sint et molestiae non recusandae.</p></article>
  <article class="abs member" style="left:712px;top:792px"><h3 class="member-name">Tianyu Zhou</h3><p class="member-role">Undergraduate researcher</p><p class="member-bio">Temporibus autem quibusdam et aut officiis debitis aut rerum necessitatibus saepe eveniet ut et voluptates repudiandae sint et molestiae non recusandae.</p></article>
</main>

<section>
  <div class="abs band-shade"></div>
  <div class="abs testimonial-band"></div>
  <div class="abs quote-badge">&ldquo;</div>
  <div class="abs portrait-frame"><div class="portrait" role="img" aria-label="Portrait photo of the quoted researcher"></div></div>
  <blockquote class="abs quote-text">Sed ut perspiciatis unde omnis iste natus sit voluptatem accusantium doloremque laudantium, totam rem aperiam, eaque ipsa quae ab illo inventore veritatis et quasi . Sed ut perspiciatis unde omnis iste natus sit voluptatem accusantium.</blockquote>
  <div class="abs quote-author"><div class="sig">- Jon Dale</div><div class="org">Lorem Ipsum Elit</div></div>
  <div class="abs slider-dots"><span></span><span></span><span></span></div>
  <div class="abs social"><span class="label">Get Social</span><span class="icon"></span><span class="icon"></span><span class="icon"></span><span class="icon alt"></span><span class="icon alt"></span></div>
  <div class="abs divider"></div>

  <div class="abs newsletter"><h3>Subscribe to our newsletter</h3><p>Lorem Ipsum Consectetur Adipiscing Elit</p></div>
  <div class="abs newsletter-input"></div>
  <p class="abs newsletter-note">Sed ut perspiciatis unde omnis iste natus sit voluptatem accusantium. Sed ut perspiciatis unde omnis.</p>
  <div class="abs newsletter-button">SUBSCRIBE</div>
</section>

<footer class="abs site-footer">
  <span style="left:132px">Address: 4420 Harbor Tower, Lakeside City, P.O. Box 550120, Westland</span>
  <span style="left:465px">Terms of Use | Privacy Policy</span>
  <span style="left:634px">Copyright Speech, Thought and Nerve Lab, SoTeN© 2014. All Rights Reserved.</span>
</footer>

</body>
</html>
```